Quillaven Shampoo

Quillaven shampoo is aimed to be a "novelty" item, with an intriguing mix of ingredients including but not limited to CBD & caffeine. We want a design that has a unique way of portraying "quillaven". Get creative with this one. We want the designers to get creative and think outside of the box, and maybe even get a little crazy (but not too crazy), because that's what the premise of the shampoo is; out of the box thinking -- "quillaven". Try to incorporate what you think of when you hear the word quillaven.

On the front of the bottle is where the main design will be shown. On the back will be the ingredients list, and will have a bit more information. The design should flow well with a darkish-brown bottle, pictured in the attachments called "bottle-size-template".

Avoid simple designs. We want our shampoo to stand out, not stand on the shelves. Get creative. IMPORTANT NOTE: Please do not use / inspire from the attachments called "bottle-size-template", as these are to show you what the bottle looks like, and what the label will look like on the bottle. DO NOT MAKE YOUR DESIGN BASED FROM THOSE ATTACHMENTS!

If you are feeling like a winner, you can even insert the correct ingredients list: Purified water (aqua), pure virgin hemp seed oil, green tea essential oil, green tea extract, aloe vera, ginseng extract, cam-phor essential oil, glycerin(vegetable), borage seed oil, lauryl glucoside, coconut oil, yucca extract, dermochlorella extract(seaweed based), nettle extract, coco glucoside, jojoba oil, awapuhi, soluble natural plant collagen, wheat germ glycerides (gluten free), echinacea extract, licorice root extract, cocoa butter, ivy extract, soy protein non-GMO), ascorbyl tetraisopalmitate (palm based), golden seal extract, behenic acid (natural based) guar gum, ylang ylang extract, sea salt.

```html
<!DOCTYPE html>
<html lang="en">
<head>
<meta charset="UTF-8">
<title>Quillaven Hair Shampoo Label</title>
<link href="https://fonts.googleapis.com/css2?family=Open+Sans:wght@400;600&display=swap" rel="stylesheet">
<style>
  :root {
    --leaf-green: #3db54a;
    --leaf-green-light: #52c45c;
    --glow-green: #2fd14a;
    --deep-dark: #0b120d;
    --white: #ffffff;
    --page: #d6d7d9;
  }
  * { margin: 0; padding: 0; box-sizing: border-box; }
  html, body {
    width: 1200px; height: 568px; overflow: hidden;
    background: var(--page);
    font-family: "Open Sans", Arial, sans-serif;
  }
  .label {
    position: absolute; left: 20px; top: 77px;
    width: 1160px; height: 414px;
    background: var(--white);
  }
  .side-band {
    position: absolute; top: 0; width: 127px; height: 414px;
    background: var(--leaf-green);
  }
  .side-band--left { left: 0; }
  .side-band--right { left: 1033px; }
  .brain-art {
    position: absolute; left: 13px; top: 18px; width: 102px; height: 378px;
    border-radius: 48% / 30%;
    background: var(--leaf-green-light);
    border: 3px solid var(--white);
  }
  .main-panel {
    position: absolute; left: 131px; top: 0; width: 899px; height: 414px;
    background:
      radial-gradient(ellipse 260px 220px at 676px 202px, rgba(120,255,140,0.85) 0%, rgba(47,209,74,0.55) 25%, rgba(20,110,40,0.35) 55%, rgba(11,18,13,0) 100%),
      radial-gradient(ellipse 200px 180px at 270px 300px, rgba(47,209,74,0.4) 0%, rgba(11,18,13,0) 100%),
      linear-gradient(90deg, #0d1a10 0%, #1a241a 50%, #121b13 100%);
  }
  .panel-text {
    position: absolute; color: var(--white);
  }
  .intro {
    left: 13px; top: 47px; width: 406px;
    font-size: 10.6px; line-height: 13.4px; text-align: justify;
  }
  .info-box {
    position: absolute; left: 13px; border: 2px solid var(--white);
  }
  .info-box__title {
    background: var(--white); color: var(--leaf-green);
    font-size: 10px; font-weight: 600; letter-spacing: 1.5px;
    text-align: center; height: 13px; line-height: 13px;
  }
  .info-box__body {
    color: var(--white); font-size: 10.2px; line-height: 13.4px;
    padding: 3px 6px; text-align: justify;
  }
  .ingredients { top: 123px; width: 406px; height: 138px; }
  .direction { top: 266px; width: 310px; height: 68px; }
  .direction .info-box__body { text-align: left; }
  .code-slot {
    position: absolute; background: var(--white); color: var(--leaf-green);
    font-size: 10px; display: flex; align-items: center; justify-content: center;
  }
  .qr-slot { left: 267px; top: 346px; width: 57px; height: 57px; }
  .barcode-slot { left: 338px; top: 269px; width: 81px; height: 134px; }
  .barcode-slot span { transform: rotate(-90deg); white-space: nowrap; }
  .brand-box {
    position: absolute; left: 563px; top: 194px; width: 224px; height: 67px;
    border: 2px solid var(--white); text-align: center; color: var(--white);
  }
  .brand-name { font-size: 35px; line-height: 40px; margin-top: 4px; font-weight: 400; }
  .brand-sub { font-size: 18px; line-height: 18px; }
  .claim {
    left: 560px; top: 321px; width: 230px; text-align: center;
    font-size: 13.5px;
  }
  .claim-rule {
    position: absolute; left: 598px; top: 343px; width: 154px; height: 1px;
    background: var(--white);
  }
  .specs {
    left: 560px; top: 350px; width: 230px; text-align: center;
    font-size: 13px; line-height: 16px;
  }
</style>
</head>
<body>
  <div class="label">
    <div class="side-band side-band--left">
      <div class="brain-art" role="img" aria-label="White line drawing of a brain seen from above"></div>
    </div>

    <div class="main-panel" role="img" aria-label="Dark background with a glowing green light burst behind a circuit-like brain">
      <p class="panel-text intro">This product is specially made with hemp seed oil, which is know for its nutritional and medicinal properties. This ingredient has been rediscovered as a beauty aid due to its moisturizing and anti-again effects. it is a rich source of essential fatty acids, including omega-3, which helps replenish and lubricates the hair the natural way.</p>

      <section class="info-box ingredients">
        <h2 class="info-box__title">INGREDIENTS LIST:</h2>
        <p class="info-box__body">Purified water (aqua), pure virgin hemp seed oil, green tea essential oil, green tea extract, aloe vera, ginseng extract, cam-phor essential oil, glycerin (vegetable), borage seed oil, lauryl glucoside, coconut oil, yucca extract, dermochlorella extract (seaweed based), nettle extract, coco glucoside, jojoba oil, awapuhi, soluble natural plant collagen, wheat germ glycerides (gluten free), echinacea extract, licorice root extract, cocoa butter, ivy extract, soy protein non-GMO), ascorbyl tetraisopalmitate (palm based), golden seal extract, behenic acid (natural based) guar gum, ylang ylang extract, sea salt.</p>
      </section>

      <section class="info-box direction">
        <h2 class="info-box__title">DIRECTION</h2>
        <p class="info-box__body">Apply hemp Shampoo to wet hair. Massage into scalp and hair, leaves for 2­3 minutes. Rinse and repeat if necessary. Recommended for daily use with Hemp Conditioner.</p>
      </section>

      <div class="code-slot qr-slot">QR</div>
      <div class="code-slot barcode-slot"><span>Bar code</span></div>

      <div class="brand-box">
        <h1 class="brand-name">quillaven</h1>
        <p class="brand-sub">Hair Shampoo</p>
      </div>

      <p class="panel-text claim">Strengthnes Weak Hair</p>
      <div class="claim-rule"></div>
      <p class="panel-text specs">For All Hair Types<br>500ml/17.7 fl.oz</p>
    </div>

    <div class="side-band side-band--right">
      <div class="brain-art" role="img" aria-label="White line drawing of a brain seen from above"></div>
    </div>
  </div>
</body>
</html>
```